The Green Sprout Path Website Design

I have hosting set up through Hostwell but need Web Design for a new company called The Green Sprout Path. I am a holistic health coach helping individuals and groups achieve optimum health through the elimination of processed foods, GMOs, animal foods and chemical toxins in foods, beauty and household products and the promotion of a plant focused diet. I provide education and coaching programs to ensure success. The site should include my logo, the colors of black, white, orange and green and convey a simple, natural and friendly tone. My goal is to be a friendly resource to those who want or need to transition to a vegan lifestyle but don't want to feel judged or the need to be perfect to heal and make a difference. Progress vs perfection.

The tabs would be: Home About Services Recipes Resources (Things I Love) I.e affiliate links Contact Possibly a calendar of events As for products, they would be simple ebooks or 30 day programs delivered electronically. They are still in development. I will have a link to a free book excerpt for opting into my mailing list. You can see a site I built through my school's hosting for a basic example at Lorianbcastell.example While I like the basic bones of it, I wanted something more robust and not tied to the school.

```html
<!DOCTYPE html>
<html lang="en">
<head>
<meta charset="utf-8">
<title>The Green Sprout Path</title>
<link href="https://fonts.googleapis.com/css2?family=Open+Sans:wght@300;400&family=Arimo:wght@400&display=swap" rel="stylesheet">
<style>
:root{
  --black:#141414;
  --footer:#111415;
  --white:#ffffff;
  --green:#4e8a10;
  --green-light:#8fbf3a;
  --orange:#e9a11a;
  --orange-band:#df9411;
  --grey-band:#e6e6e6;
  --text:#555555;
  --text-dark:#111111;
  --rule:#cfcfcf;
  --icon:#666666;
}
*{margin:0;padding:0;box-sizing:border-box}
html,body{width:1200px;height:2169px;overflow:hidden;background:var(--white)}
body{position:relative;font-family:"Arimo",Arial,sans-serif;color:var(--text)}
.abs{position:absolute}
.heading{font-family:"Open Sans",Arial,sans-serif;font-weight:300;color:var(--green)}

/* header */
.site-header{left:0;top:0;width:1200px;height:87px;background:var(--black)}
.brand{left:171px;top:20px;display:flex;align-items:center;gap:8px}
.brand-dot{width:22px;height:22px;border-radius:50%;background:var(--orange)}
.brand-name{font-family:"Open Sans",Arial,sans-serif;font-size:12px;color:var(--green-light)}
.main-nav a{position:absolute;top:37px;font-size:12px;color:#d0d0d0;text-decoration:none;transform:translateX(-50%);white-space:nowrap}

/* hero */
.hero{left:0;top:87px;width:1200px;height:409px;background:linear-gradient(90deg,#b9e3a0 0%,#e9f5e2 30%,#f7f7f5 48%,#f1f1ef 100%)}
.hero-photo{left:477px;top:87px;width:723px;height:409px;background:radial-gradient(ellipse at 70% 40%,#e8c6ac 0%,#d9b398 25%,#f2efe9 55%,#f7f7f5 100%)}
.hero-title{left:171px;top:164px;font-size:43px;white-space:nowrap}
.hero-sub{left:171px;top:225px;font-family:"Open Sans",Arial,sans-serif;font-weight:400;font-size:37px;color:var(--text-dark);white-space:nowrap}
.hero-text{left:171px;top:281px;width:370px;font-size:13px;line-height:23px;color:var(--text-dark)}
.btn{display:flex;align-items:center;justify-content:center;background:var(--orange);color:var(--white);font-size:12.5px;text-transform:uppercase;border-radius:3px}
.hero-btn{left:171px;top:370px;width:232px;height:48px}
.hero-arrow{left:68px;top:279px}

/* what we do */
.section-title{left:0;width:1200px;text-align:center;font-size:29px}
.section-text{left:231px;width:738px;text-align:center;font-size:12px;line-height:23px}
.rule{left:188px;top:659px;width:817px;height:1px;background:var(--rule)}
.service-icon{top:690px}
.service-title{top:696px;font-family:"Open Sans",Arial,sans-serif;font-size:16px;color:var(--green)}
.service-text{top:725px;width:150px;font-size:10.5px;line-height:19px}

/* about */
.about-band{left:0;top:830px;width:1200px;height:364px;background:var(--grey-band)}
.about-photo{left:171px;top:892px;width:380px;height:240px;background:linear-gradient(120deg,#f4f4f4 0%,#e7d6c8 45%,#f3f3f3 75%,#e8efe0 100%)}
.about-title{left:590px;top:884px;font-size:29px;white-space:nowrap}
.about-text{left:590px;width:420px;font-size:11px;line-height:22px}
.about-btn{left:593px;top:1086px;width:153px;height:36px;font-size:11.5px}

/* stories */
.story-photo{top:1362px;width:273px;height:195px}
.story-caption{top:1573px;width:273px;text-align:center;font-size:12px;color:var(--text)}
.story-link{top:1597px;width:273px;text-align:center;font-size:12px;color:var(--orange)}

/* testimonials */
.testimonial-band{left:0;top:1666px;width:1200px;height:381px;background:var(--orange-band)}
.testimonial-title{color:var(--white);font-weight:400}
.quote-mark{font-family:Georgia,serif;font-size:36px;color:var(--white);line-height:1}
.quote-text{left:262px;top:1790px;width:676px;text-align:center;font-size:12px;line-height:23px;color:var(--white)}
.avatar{left:474px;top:1914px;width:82px;height:82px;border-radius:50%;background:radial-gradient(circle at 50% 45%,#f3d7c2 0%,#e6c19c 40%,#fafafa 72%);border:3px solid var(--white)}
.author-name{left:577px;top:1931px;font-size:12.5px;color:var(--white)}
.author-date{left:577px;top:1955px;font-size:12.5px;font-style:italic;color:var(--white)}

/* footer */
.site-footer{left:0;top:2047px;width:1200px;height:122px;background:var(--footer)}
.footer-nav a{position:absolute;top:2088px;font-size:10.5px;color:#aaaaaa;text-decoration:none;white-space:nowrap}
.copyright{left:175px;top:2116px;font-size:10.5px;color:#999999}
.social{top:2088px;width:40px;height:40px;border-radius:50%;border:1.5px solid #555555}
</style>
</head>
<body>

<header class="abs site-header">
  <div class="abs brand">
    <span class="brand-dot"></span>
    <span class="brand-name">The Green Sprout Path</span>
  </div>
  <nav class="main-nav">
    <a style="left:486px" href="#">Home</a>
    <a style="left:572px" href="#">About us</a>
    <a style="left:665px" href="#">Services</a>
    <a style="left:759px" href="#">Solutions</a>
    <a style="left:863px" href="#">Testimonials</a>
    <a style="left:970px" href="#">Contact us</a>
  </nav>
</header>

<section>
  <div class="abs hero"></div>
  <div class="abs hero-photo" role="img" aria-label="Photo of a smiling woman eating a fresh salad from a fork"></div>
  <svg class="abs hero-arrow" width="48" height="48" viewBox="0 0 48 48" aria-hidden="true">
    <circle cx="24" cy="24" r="22" fill="none" stroke="#8fae7e" stroke-width="2"/>
    <path d="M12 24 L32 13 L27 24 L32 35 Z" fill="#8fae7e"/>
  </svg>
  <h1 class="abs heading hero-title">Progress vs perfection</h1>
  <h2 class="abs hero-sub">The Green Sprout Path</h2>
  <p class="abs hero-text">Iam a holistic health coach helping individuals and groups achieve optimum health through the elimination of processed foods, GMOs, animal foods and chemical toxins in foods.</p>
  <a class="abs btn hero-btn">Click here for more info</a>
</section>

<section>
  <h2 class="abs heading section-title" style="top:533px">What we do?</h2>
  <p class="abs section-text" style="top:589px">Lorem Ipsum is simply dummy text of the printing and typesetting industry. Lorem Ipsum has been the industry's standard dummy text ever since the 1500s, when an unknown printer took a galley of type and scrambled it to make a type specimen book.</p>
  <div class="abs rule"></div>

  <svg class="abs service-icon" style="left:175px" width="36" height="36" viewBox="0 0 36 36" aria-hidden="true" fill="none" stroke="var(--icon)" stroke-width="2" stroke-linecap="round">
    <path d="M4 32 L28 8"/><path d="M22 14 L20 8"/><path d="M22 14 L28 16"/><path d="M17 19 L15 13"/><path d="M17 19 L23 21"/><path d="M12 24 L10 18"/><path d="M12 24 L18 26"/>
  </svg>
  <h3 class="abs service-title" style="left:224px">Services 01</h3>
  <p class="abs service-text" style="left:224px">uncover many web sites still in their infancy. Various versions have evolved...</p>

  <svg class="abs service-icon" style="left:398px" width="36" height="36" viewBox="0 0 36 36" aria-hidden="true" fill="none" stroke="var(--icon)" stroke-width="2.2" stroke-linecap="round">
    <circle cx="21" cy="13" r="9"/><path d="M14 20 L5 30"/>
  </svg>
  <h3 class="abs service-title" style="left:450px">Services 02</h3>
  <p class="abs service-text" style="left:450px">uncover many web sites still in their infancy. Various versions have evolved...</p>

  <svg class="abs service-icon" style="left:622px" width="36" height="36" viewBox="0 0 36 36" aria-hidden="true" fill="none" stroke="var(--icon)" stroke-width="3" stroke-linecap="round">
    <path d="M6 30 L30 6"/><path d="M6 6 L30 30"/><path d="M24 4 L32 12" stroke-width="4"/><path d="M3 10 L10 3" stroke-width="4"/>
  </svg>
  <h3 class="abs service-title" style="left:674px">Services 03</h3>
  <p class="abs service-text" style="left:674px">uncover many web sites still in their infancy. Various versions have evolved...</p>

  <svg class="abs service-icon" style="left:843px" width="30" height="36" viewBox="0 0 30 36" aria-hidden="true" fill="none" stroke="var(--icon)" stroke-width="2">
    <path d="M15 34 C6 22 3 17 3 13 A12 12 0 0 1 27 13 C27 17 24 22 15 34 Z"/><circle cx="15" cy="13" r="4"/>
  </svg>
  <h3 class="abs service-title" style="left:889px">Services 04</h3>
  <p class="abs service-text" style="left:889px">uncover many web sites still in their infancy. Various versions have evolved...</p>
</section>

<section>
  <div class="abs about-band"></div>
  <div class="abs about-photo" role="img" aria-label="Photo of a woman holding a green apple and a measuring tape"></div>
  <h2 class="abs heading about-title">About The Green Sprout Path</h2>
  <p class="abs about-text" style="top:934px">Lorem Ipsum is simply dummy text of the printing and typesetting industry. Lorem Ipsum has been the industry's standard dummy text ever since the 1500s, when an unknown printer took a galley of type and scrambled it to make a type specimen.</p>
  <p class="abs about-text" style="top:1020px">Lorem Ipsum is simply dummy text of the printing and typesetting industry. Lorem Ipsum has been the industry's standard dummy text...</p>
  <a class="abs btn about-btn">Read more info</a>
</section>

<section>
  <h2 class="abs heading section-title" style="top:1234px">Successful Stories</h2>
  <p class="abs section-text" style="top:1287px">Lorem Ipsum is simply dummy text of the printing and typesetting industry. Lorem Ipsum has been the industry's standard dummy text ever since the 1500s, when an unknown printer took a galley of type and scrambled it to make a type specimen book.</p>

  <div class="abs story-photo" style="left:171px;background:linear-gradient(135deg,#8fd3f0 0%,#4bb6e3 45%,#e8c3a3 70%,#9fd8ef 100%)" role="img" aria-label="Photo of a slim waist with a measuring tape"></div>
  <p class="abs story-caption" style="left:171px">Lorem Ipsum is simply dummy</p>
  <p class="abs story-link" style="left:171px">Click to Read More</p>

  <div class="abs story-photo" style="left:463px;background:radial-gradient(circle at 50% 50%,#c94a2e 0%,#6f9a2a 40%,#3f6e1c 75%,#2c4a18 100%)" role="img" aria-label="Photo of a fresh Greek salad with tomatoes, olives and feta"></div>
  <p class="abs story-caption" style="left:463px">Lorem Ipsum is simply dummy</p>
  <p class="abs story-link" style="left:463px">Click to Read More</p>

  <div class="abs story-photo" style="left:756px;background:linear-gradient(135deg,#f4f4f4 0%,#e4c2a4 45%,#b9c4cf 75%,#eeeeee 100%)" role="img" aria-label="Photo of a smiling man eating a salad"></div>
  <p class="abs story-caption" style="left:756px">Lorem Ipsum is simply dummy</p>
  <p class="abs story-link" style="left:756px">Click to Read More</p>
</section>

<section>
  <div class="abs testimonial-band"></div>
  <h2 class="abs heading section-title testimonial-title" style="top:1711px">Testimonials</h2>
  <svg class="abs" style="left:148px;top:1832px" width="14" height="26" viewBox="0 0 14 26" aria-hidden="true"><path d="M12 2 L3 13 L12 24" fill="none" stroke="#f0c070" stroke-width="1.5"/></svg>
  <svg class="abs" style="left:1038px;top:1832px" width="14" height="26" viewBox="0 0 14 26" aria-hidden="true"><path d="M2 2 L11 13 L2 24" fill="none" stroke="#f0c070" stroke-width="1.5"/></svg>
  <span class="abs quote-mark" style="left:237px;top:1770px">“</span>
  <p class="abs quote-text">It is a long established fact that a reader will be distracted by the readable content of a page when looking at its layout. The point of using Lorem Ipsum is that it has a more-or-less normal distribution of letters, as opposed to using 'Content here, content here', making it look like readable English. Many desktop publishing packages and web page editors now use Lorem Ipsum as their default model text, and a search...</p>
  <span class="abs quote-mark" style="left:946px;top:1868px">”</span>
  <div class="abs avatar" role="img" aria-label="Portrait photo of the client giving the testimonial"></div>
  <p class="abs author-name">Mira Tallen</p>
  <p class="abs author-date">Posted on 27 march 2014</p>
</section>

<footer class="abs site-footer"></footer>
<nav class="footer-nav">
  <a style="left:175px" href="#">Home</a>
  <a style="left:247px" href="#">About us</a>
  <a style="left:334px" href="#">Services</a>
  <a style="left:419px" href="#">Solutions</a>
  <a style="left:507px" href="#">Testimonials</a>
  <a style="left:610px" href="#">Contact us</a>
</nav>
<p class="abs copyright">Copyrights © 2014. The Green Sprout Path. All Rights Reserved</p>
<span class="abs social" style="left:839px" aria-label="Social link"></span>
<span class="abs social" style="left:888px" aria-label="Social link"></span>
<span class="abs social" style="left:937px" aria-label="Social link"></span>
<span class="abs social" style="left:988px" aria-label="Social link"></span>

</body>
</html>
```